Marrowick Billboards

We already hava a logo, slogan and general theme, we are looking for 2 to 3 billboard designs for out Recreational-Use Retail Cannabis Dispensary in NY state. We would like for the billboard to be a "Space" theme with a realistic-looking astronaut, we cannot have any "cartoon-like" images that would be attractive to children per state regulations. We would like the following wording included:
Marrowick Cannabis Company - Oswego , slogan is "Products out of this world" , address of 871 Tallow Lane - Oswego, Free Delivery - Orders over $150 . Our primary brand color is lime green.

```html
<!DOCTYPE html>
<html lang="en">
<head>
<meta charset="utf-8">
<title>Marrowick Cannabis Company – Billboard</title>
<link href="https://fonts.googleapis.com/css2?family=Anton&family=Poppins:wght@600;700;800&family=Cinzel:wght@500&display=swap" rel="stylesheet">
<style>
  :root {
    --backdrop: #adadad;
    --space-dark: #05080a;
    --space-green: #1f4a12;
    --nebula: #2f6b2a;
    --lime: #8fd614;
    --lime-bright: #9be21c;
    --ink: #0b0f08;
    --white: #ffffff;
    --bar: #070a06;
    --suit-orange: #c8642a;
    --suit-violet: #5b2a7a;
  }
  * { margin: 0; padding: 0; box-sizing: border-box; }
  html, body { width: 1200px; height: 482px; overflow: hidden; }
  body { background: var(--backdrop); position: relative; font-family: "Poppins", sans-serif; }

  .billboard {
    position: absolute; left: 94px; top: 94px; width: 1014px; height: 296px;
    overflow: hidden; background: var(--space-dark);
  }
  .space-scene {
    position: absolute; inset: 0;
    background:
      radial-gradient(ellipse 260px 160px at 400px 200px, var(--nebula) 0%, rgba(47,107,42,0) 70%),
      radial-gradient(ellipse 360px 120px at 470px 230px, rgba(60,140,40,.55) 0%, rgba(60,140,40,0) 75%),
      radial-gradient(ellipse 200px 140px at 120px 60px, rgba(40,70,90,.5) 0%, rgba(40,70,90,0) 70%),
      linear-gradient(90deg, #07100a 0%, var(--space-green) 45%, #0c1a0c 70%, #050906 100%);
  }
  .astronaut-art {
    position: absolute; left: 312px; top: 18px; width: 250px; height: 214px;
    border-radius: 40% 40% 30% 30%;
    background: radial-gradient(ellipse at 50% 40%, var(--suit-orange) 0%, var(--suit-violet) 55%, rgba(91,42,122,0) 75%);
    opacity: .8;
  }

  .brand-name {
    position: absolute; left: 28px; top: 26px; width: 300px;
    font-family: "Cinzel", serif; font-weight: 500; color: var(--white);
    text-align: center; line-height: 1.15;
  }
  .brand-name .line-main { display: block; font-size: 31px; }
  .brand-name .line-sub { display: block; font-size: 19px; }
  .brand-name .line-town { display: block; font-size: 19px; margin-top: 4px; }

  .delivery { position: absolute; left: 28px; top: 150px; }
  .delivery-icon { position: absolute; left: 0; top: 7px; width: 38px; height: 22px; }
  .delivery-free {
    position: absolute; left: 40px; top: -2px;
    font-weight: 800; font-size: 38px; line-height: 1; color: var(--lime);
  }
  .delivery-label {
    position: absolute; left: 1px; top: 37px;
    font-weight: 800; font-size: 23px; line-height: 1; color: var(--white);
  }

  .order-badge {
    position: absolute; left: 181px; top: 141px; width: 139px; height: 78px;
    border: 2px solid var(--lime); border-radius: 10px; background: var(--ink); overflow: hidden;
  }
  .order-badge-head {
    background: var(--lime); color: var(--ink);
    font-weight: 800; font-size: 15px; text-align: center; padding: 3px 0 2px;
  }
  .order-badge-amount {
    color: var(--white); font-weight: 800; font-size: 44px; line-height: 1;
    text-align: center; margin-top: 4px;
  }
  .order-badge-amount sup { font-size: 22px; vertical-align: 18px; }

  .slogan { position: absolute; left: 574px; top: 28px; width: 392px; text-align: center; font-family: "Anton", sans-serif; line-height: 1; }
  .slogan-main { display: block; font-size: 76px; color: var(--lime-bright); letter-spacing: 1px; }
  .slogan-sub { display: block; font-size: 43px; color: var(--white); margin-top: 2px; }

  .address {
    position: absolute; left: 673px; top: 156px; width: 360px; height: 66px;
    background: var(--lime); border-radius: 12px 0 0 12px;
    display: flex; align-items: center; padding-left: 12px; gap: 6px;
    color: var(--ink); font-weight: 700; font-size: 24px; line-height: 1.05;
  }
  .address svg { width: 18px; height: 26px; flex: none; align-self: flex-start; margin-top: 8px; }

  .contact-bar {
    position: absolute; left: 0; bottom: 0; width: 100%; height: 66px; background: var(--bar);
    display: flex; align-items: center; color: var(--white); font-weight: 700;
  }
  .contact-phone { position: absolute; left: 32px; display: flex; align-items: center; gap: 8px; font-size: 33px; }
  .contact-web { position: absolute; left: 408px; display: flex; align-items: center; gap: 12px; font-size: 33px; }
  .contact-web .accent { color: var(--lime); }
  .contact-bar svg { width: 26px; height: 26px; }
</style>
</head>
<body>
  <main class="billboard">
    <div class="space-scene" role="img" aria-label="Deep space background with green nebula and stars"></div>
    <div class="astronaut-art" role="img" aria-label="Realistic astronaut in a colourful suit floating in space"></div>

    <div class="brand-name">
      <span class="line-main">Marrowick</span>
      <span class="line-sub">Cannabis Company</span>
      <span class="line-town">Oswego</span>
    </div>

    <div class="delivery">
      <svg class="delivery-icon" viewBox="0 0 38 22" aria-hidden="true">
        <rect x="8" y="2" width="18" height="13" fill="#8fd614"/>
        <path d="M26 6h6l5 5v4H26z" fill="#8fd614"/>
        <circle cx="13" cy="17" r="3.5" fill="#8fd614" stroke="#05080a" stroke-width="1.5"/>
        <circle cx="31" cy="17" r="3.5" fill="#8fd614" stroke="#05080a" stroke-width="1.5"/>
        <rect x="0" y="5" width="6" height="2" fill="#8fd614"/>
        <rect x="2" y="10" width="5" height="2" fill="#8fd614"/>
      </svg>
      <span class="delivery-free">FREE</span>
      <span class="delivery-label">DELIVERY</span>
    </div>

    <div class="order-badge">
      <div class="order-badge-head">ORDERS OVER</div>
      <div class="order-badge-amount"><sup>$</sup>150</div>
    </div>

    <h1 class="slogan">
      <span class="slogan-main">PRODUCTS</span>
      <span class="slogan-sub">OUT OF THIS WORLD</span>
    </h1>

    <div class="address">
      <svg viewBox="0 0 18 26" aria-hidden="true">
        <path d="M9 1C4.6 1 1 4.5 1 9c0 6 8 16 8 16s8-10 8-16c0-4.5-3.6-8-8-8z" fill="none" stroke="#0b0f08" stroke-width="2.4"/>
        <circle cx="9" cy="9" r="3" fill="#0b0f08"/>
      </svg>
      <span>871 Tallow Lane<br>- Oswego</span>
    </div>

    <footer class="contact-bar">
      <div class="contact-phone">
        <svg viewBox="0 0 24 24" aria-hidden="true">
          <path d="M6.6 10.8a15 15 0 0 0 6.6 6.6l2.2-2.2c.3-.3.7-.4 1-.2 1.1.4 2.3.6 3.6.6.6 0 1 .4 1 1V20c0 .6-.4 1-1 1A17 17 0 0 1 3 4c0-.6.4-1 1-1h3.5c.6 0 1 .4 1 1 0 1.3.2 2.5.6 3.6.1.3 0 .7-.2 1z" fill="#8fd614"/>
        </svg>
        <span>(315) 555-0142</span>
      </div>
      <div class="contact-web">
        <svg viewBox="0 0 24 24" aria-hidden="true">
          <circle cx="12" cy="12" r="10" fill="none" stroke="#8fd614" stroke-width="2"/>
          <ellipse cx="12" cy="12" rx="4.5" ry="10" fill="none" stroke="#8fd614" stroke-width="2"/>
          <path d="M2 12h20M4 7h16M4 17h16" stroke="#8fd614" stroke-width="2"/>
        </svg>
        <span>WWW.<span class="accent">MARROWICK</span>.COM</span>
      </div>
    </footer>
  </main>
</body>
</html>
```